Post card for Tax Preparation Services

Bramble Ledger, a accounting and tax solution firm is in need of a postcard to send to people who have moved into the area in the last year. The goal is to market our tax preparation services. More information on our business and services can be found on our website: www.brambleledger-example.com

Return address:
4817 Harrow Mill Pkwy
Bldg 300, Ste 410
Woodstock, GA 30274

Phone: (678) 555-7SUM

Please submit copies of front and back design in one submisstion. Do not submit duplicate designs.

Target Market(s)

People who have moved within 2 miles of our office

Industry/Entity Type

Accounting

Colors
6b449b
fbee3e

Requirements
Must have
• Logo
• Schedule Online
• Mention this postcard Receive $25.00 off tax prep
• Colors Gold #c6A734 and Purple #5f1547 to match logo
Should not have
• No cartoony feel

```html
<!DOCTYPE html>
<html lang="en">
<head>
<meta charset="utf-8">
<title>Bramble Ledger – Tax Preparation Postcard</title>
<link href="https://fonts.googleapis.com/css2?family=Montserrat:ital,wght@0,500;0,700;0,800;1,500&family=Open+Sans:wght@400;600&display=swap" rel="stylesheet">
<style>
  :root{
    --purple:#5f1547;
    --purple-deep:#3d0d2e;
    --gold:#c6a734;
    --gold-light:#e2c65a;
    --ink:#231f20;
    --white:#ffffff;
    --stage:#c9c9c9;
    --muted:#6d6d6d;
  }
  *{box-sizing:border-box;margin:0;padding:0}
  html,body{width:831px;height:1200px;overflow:hidden}
  body{background:var(--stage);font-family:"Open Sans",Arial,sans-serif;position:relative}
  .card{position:absolute;left:36px;width:762px;background:var(--white);overflow:hidden;box-shadow:0 3px 10px rgba(0,0,0,.25)}
  .card--front{top:22px;height:568px}
  .card--back{top:623px;height:554px}

  /* brand lockup */
  .brand{position:absolute;display:flex;align-items:center;gap:10px}
  .brand__mark{width:30px;height:30px;background:var(--gold)}
  .brand__text{display:flex;flex-direction:column}
  .brand__name{font-family:"Montserrat",Arial,sans-serif;font-weight:800;color:var(--purple);font-size:26px;letter-spacing:.5px;text-transform:uppercase;line-height:1}
  .brand__tag{font-family:"Montserrat",Arial,sans-serif;font-weight:700;color:var(--purple);font-size:10.5px;letter-spacing:1.4px;text-transform:uppercase;margin-top:4px}

  /* front */
  .offer{position:absolute;left:22px;top:0;width:92px;height:104px;background:var(--purple);color:var(--white);text-align:center;font-family:"Montserrat",Arial,sans-serif;padding-top:12px}
  .offer__amount{font-size:34px;font-weight:800;line-height:1;color:var(--gold-light)}
  .offer__amount sup{font-size:17px;vertical-align:top}
  .offer__off{font-size:20px;font-weight:800;letter-spacing:1px}
  .offer__label{font-size:11px;font-weight:700;letter-spacing:1px;margin-top:6px}
  .card--front .brand{left:318px;top:22px}

  .photo{position:absolute;background:linear-gradient(135deg,#d9cfc6 0%,#b8a79b 45%,#7d6a63 100%)}
  .photo--front{left:0;top:96px;width:400px;height:346px}

  .hero{position:absolute;left:400px;top:96px;width:362px;height:346px;background:var(--purple)}
  .hero__edge{position:absolute;left:-30px;top:0}
  .hero__title{position:absolute;left:26px;top:22px;right:18px;font-family:"Montserrat",Arial,sans-serif;font-weight:800;color:var(--white);font-size:21px;line-height:1.15;text-transform:uppercase}
  .hero__sub{position:absolute;left:26px;top:52px;font-family:"Montserrat",Arial,sans-serif;font-weight:700;color:var(--gold-light);font-size:14px;letter-spacing:.4px;text-transform:uppercase}
  .services__bar{position:absolute;left:0;top:98px;width:260px;height:30px;background:var(--gold);color:var(--white);font-family:"Montserrat",Arial,sans-serif;font-weight:700;font-size:12.5px;letter-spacing:.6px;padding:8px 0 0 26px;text-transform:uppercase}
  .services__list{position:absolute;left:26px;top:146px;width:320px;display:grid;grid-template-columns:1fr 1fr;gap:14px 16px;list-style:none}
  .services__item{display:flex;gap:6px;color:var(--white);font-size:11.5px;line-height:1.3}
  .services__item svg{flex:0 0 11px;margin-top:3px}

  .callout{position:absolute;left:0;top:442px;width:400px;height:126px;background:var(--ink);color:var(--white);padding:22px 0 0 40px}
  .callout__lead{font-size:10.5px;font-style:italic}
  .callout__phone{font-family:"Montserrat",Arial,sans-serif;font-weight:800;font-size:42px;letter-spacing:.5px;margin-top:6px}
  .schedule{position:absolute;left:420px;top:470px}
  .schedule__title{font-family:"Montserrat",Arial,sans-serif;font-weight:800;font-size:34px;color:var(--gold);line-height:1}
  .schedule__url{font-family:"Montserrat",Arial,sans-serif;font-weight:700;font-size:17px;color:var(--purple);margin-top:10px}

  /* back */
  .card--back .brand{left:30px;top:30px}
  .return-address{position:absolute;left:450px;top:38px;font-size:12px;line-height:1.45;color:var(--ink)}
  .stamp{position:absolute;right:34px;top:30px;width:80px;height:90px;background:#e4e4e4}
  .info{position:absolute;left:0;top:110px;width:420px;height:444px;background:var(--purple);color:var(--white)}
  .info__title{position:absolute;left:28px;top:24px;font-family:"Montserrat",Arial,sans-serif;font-weight:700;color:var(--gold-light);font-size:18px;text-transform:uppercase}
  .info__body{position:absolute;left:28px;top:58px;width:366px;font-size:10.5px;line-height:1.5}
  .info__body p+p{margin-top:8px}
  .info__note{position:absolute;left:0;top:238px;width:420px;height:62px;border-top:2px solid var(--gold);border-bottom:2px solid var(--gold);display:flex;align-items:center;justify-content:space-between;padding:0 16px 0 28px}
  .info__note p{font-family:"Montserrat",Arial,sans-serif;font-style:italic;font-weight:500;font-size:14px;width:310px;line-height:1.3}
  .photo--back{left:0;top:320px;width:160px;height:124px}
  .contact{position:absolute;left:176px;top:322px;font-size:11px;line-height:1.55}
  .contact__name{font-family:"Montserrat",Arial,sans-serif;font-weight:700;font-size:19px;color:var(--gold-light);margin-bottom:4px}
</style>
</head>
<body>

<section class="card card--front" aria-label="Postcard front">
  <div class="offer">
    <div class="offer__amount"><sup>$</sup>25</div>
    <div class="offer__off">OFF</div>
    <div class="offer__label">TAX PREP</div>
  </div>

  <div class="brand">
    <span class="brand__mark"></span>
    <div class="brand__text">
      <span class="brand__name">Bramble Ledger</span>
      <span class="brand__tag">Accounting &amp; Tax Solutions</span>
    </div>
  </div>

  <div class="photo photo--front" role="img" aria-label="Photo of a woman reviewing tax paperwork at a desk"></div>

  <div class="hero">
    <svg class="hero__edge" width="31" height="346" viewBox="0 0 31 346"><polygon points="30,0 31,0 31,346 0,346" fill="var(--purple)"/></svg>
    <h1 class="hero__title">Take the stress out of tax time</h1>
    <p class="hero__sub" style="top:78px">Tax Preparation &amp; Planning</p>
    <div class="services__bar" style="top:120px">Tax Preparation Services</div>
    <ul class="services__list" style="top:168px">
      <li class="services__item"><svg width="11" height="11" viewBox="0 0 11 11"><polyline points="1,6 4,9 10,1" fill="none" stroke="var(--gold)" stroke-width="2"/></svg>Individual Tax Preparation</li>
      <li class="services__item"><svg width="11" height="11" viewBox="0 0 11 11"><polyline points="1,6 4,9 10,1" fill="none" stroke="var(--gold)" stroke-width="2"/></svg>Partnership &amp; Corporate Tax Preparation</li>
      <li class="services__item"><svg width="11" height="11" viewBox="0 0 11 11"><polyline points="1,6 4,9 10,1" fill="none" stroke="var(--gold)" stroke-width="2"/></svg>Business Tax Return Preparation</li>
      <li class="services__item"><svg width="11" height="11" viewBox="0 0 11 11"><polyline points="1,6 4,9 10,1" fill="none" stroke="var(--gold)" stroke-width="2"/></svg>Estate and Succession Planning</li>
      <li class="services__item"><svg width="11" height="11" viewBox="0 0 11 11"><polyline points="1,6 4,9 10,1" fill="none" stroke="var(--gold)" stroke-width="2"/></svg>Gift &amp; Estate Tax Return Preparation</li>
      <li class="services__item"><svg width="11" height="11" viewBox="0 0 11 11"><polyline points="1,6 4,9 10,1" fill="none" stroke="var(--gold)" stroke-width="2"/></svg>Out-of-State Returns</li>
      <li class="services__item"></li>
      <li class="services__item"><svg width="11" height="11" viewBox="0 0 11 11"><polyline points="1,6 4,9 10,1" fill="none" stroke="var(--gold)" stroke-width="2"/></svg>Business Start Ups</li>
    </ul>
  </div>

  <div class="callout">
    <p class="callout__lead">If You'd Like to Receive More Information Please Call Us at:</p>
    <p class="callout__phone">(678) 555-7SUM</p>
  </div>

  <div class="schedule">
    <p class="schedule__title">SCHEDULE ONLINE</p>
    <p class="schedule__url">www.brambleledger-example.com</p>
  </div>
</section>

<section class="card card--back" aria-label="Postcard back">
  <div class="brand">
    <span class="brand__mark"></span>
    <div class="brand__text">
      <span class="brand__name">Bramble Ledger</span>
      <span class="brand__tag">Accounting &amp; Tax Solutions</span>
    </div>
  </div>

  <address class="return-address" style="font-style:normal">
    4817 Harrow Mill Pkwy<br>
    Bldg 300, Ste 410<br>
    Woodstock, GA 30274
  </address>
  <div class="stamp"></div>

  <div class="info">
    <h2 class="info__title">Tax Preparation &amp; Planning</h2>
    <div class="info__body">
      <p>These days, the majority of people and small businesses use a professional tax preparer to assist with the preparation of taxes. Even if you are just filing a simple return, the rules may change from year to year and it is easy to overlook these changes and submit an incorrect return. By doing your taxes yourself, you may also end up overlooking deductions and credits.</p>
      <p>At Bramble Ledger, our tax accountants have the expertise that is needed to help you file your returns while also helping you to minimize your tax liability with careful planning.</p>
    </div>
    <div class="info__note">
      <p>Bramble Ledger Can Also Help With Our Extensive Tax Planning Services.</p>
      <svg width="34" height="34" viewBox="0 0 34 34"><circle cx="17" cy="17" r="15" fill="none" stroke="var(--gold)" stroke-width="2"/><polyline points="14,10 21,17 14,24" fill="none" stroke="var(--gold)" stroke-width="2.5"/></svg>
    </div>
    <div class="photo photo--back" role="img" aria-label="Portrait photo of the firm's tax advisor"></div>
    <div class="contact">
      <p class="contact__name">Bramble Ledger, LLC</p>
      <p>Phone: (678) 555-7SUM</p>
      <p>Fax: (678) 555-0142</p>
      <p>E-mail: dana@brambleledger-example.com</p>
      <p>Web: www.brambleledger-example.com</p>
    </div>
  </div>
</section>

</body>
</html>
```